IT Network Consultancy - Business Card

t4 linkways is a IT network consultancy based in London. We're looking for a smart, modern and professional business card design. Our website is here: www.t4linkways.co.uk

Key things that should be included on the card (with examples):

Company Logo
Name
Position / Job Title: Network Consultant
Mobile Phone Number: +44 (0) 7700 900418
Land Line: +44 (0) 1632 960274
Email Address: name@t4linkways.co.uk
Web Site URL: www.t4linkways.co.uk

Target Market(s)

Large enterprise / global companies / corporates

Industry/Entity Type

Business

Requirements
Must have
• Incorporate our logo - which is attached to the project. They are in AI format (can be opened in Inkscape).

The design should be double sided and fit on a UK standard 85mm × 55mm card and be in a format that retains the quality when printed.
Nice to have
• The project does not have to conform to the colour of our website but this should give you inspiration of the style we like.
Should not have
• Bright colours. Pictures are not necessary.

```html
<!DOCTYPE html>
<html lang="en">
<head>
<meta charset="utf-8">
<title>linkways – Business Card</title>
<link rel="stylesheet" href="https://fonts.googleapis.com/css2?family=Lexend:wght@400&family=Lexend+Exa:wght@300;400&display=swap">
<style>
  :root {
    --slate: #4f5761;
    --slate-edge: #3a4048;
    --mark-grey: #a3a6aa;
    --paper: #ffffff;
    --ink: #2f3236;
    --ink-soft: #4a4d52;
    --gear-grey: #b4b6b9;
    --canvas: #ffffff;
  }
  * { box-sizing: border-box; margin: 0; padding: 0; }
  html, body {
    width: 1200px; height: 830px; overflow: hidden;
    background: var(--canvas);
  }
  .sheet { position: relative; width: 1200px; height: 830px; }

  .card {
    position: absolute;
    width: 533px; height: 344px;
    border-radius: 40px;
    border: 1.5px solid var(--slate-edge);
    overflow: hidden;
  }
  .card--front { background: var(--paper); }
  .card--back  { background: var(--slate); }
  .pos-a { left: 63px;  top: 61px; }
  .pos-b { left: 630px; top: 61px; }
  .pos-c { left: 63px;  top: 438px; }
  .pos-d { left: 630px; top: 438px; }

  .header-band {
    position: absolute; left: 0; top: 0;
    width: 100%; height: 105px;
    background: var(--slate);
  }

  .wordmark {
    position: absolute;
    display: flex; align-items: center; gap: 12px;
    font-family: "Lexend", sans-serif;
    font-weight: 400;
    color: var(--paper);
    letter-spacing: 0;
    white-space: nowrap;
  }
  .wordmark__square { background: var(--mark-grey); flex: none; border-radius: 50%; }
  .card--front .wordmark { left: 46px; top: 33px; font-size: 30px; }
  .card--front .wordmark__square { width: 28px; height: 28px; }
  .card--back .wordmark { left: 59px; top: 38px; font-size: 40px; }
  .card--back .wordmark__square { width: 36px; height: 36px; }

  .person-name {
    position: absolute; left: 46px; top: 158px;
    font-family: "Lexend Exa", sans-serif; font-weight: 300;
    font-size: 24px; color: var(--ink); letter-spacing: 0.5px;
    text-transform: uppercase;
  }
  .job-title {
    position: absolute; left: 46px; top: 193px;
    font-family: "Lexend Exa", sans-serif; font-weight: 300;
    font-size: 15px; color: var(--ink-soft);
  }
  .contact-list {
    position: absolute; left: 46px; top: 250px;
    list-style: none;
    font-family: "Lexend Exa", sans-serif; font-weight: 300;
    font-size: 11px; line-height: 13.5px; color: var(--ink-soft);
    white-space: nowrap;
  }
  .contact-list .label { display: inline-block; width: 74px; }

  .gear-art {
    position: absolute; left: 375px; top: 142px;
    width: 158px; height: 188px;
    background: linear-gradient(160deg, var(--gear-grey), #c9cbcd);
    border-top-left-radius: 60px;
  }

  .web-address {
    position: absolute; right: 58px; top: 240px;
    font-family: "Lexend Exa", sans-serif; font-weight: 300;
    font-size: 15px; color: var(--paper); letter-spacing: 0.5px;
    text-transform: uppercase; white-space: nowrap;
  }
  .tagline {
    position: absolute; left: 87px; top: 240px; width: 400px;
    font-family: "Lexend Exa", sans-serif; font-weight: 300;
    font-size: 12px; line-height: 14px; color: var(--paper);
  }
</style>
</head>
<body>
<main class="sheet">

  <section class="card card--front pos-a" aria-label="Front of card, version one">
    <div class="header-band">
      <div class="wordmark"><span class="wordmark__square"></span><span>linkways</span></div>
    </div>
    <h1 class="person-name">Daniel Hartley</h1>
    <p class="job-title">network consultant</p>
    <ul class="contact-list">
      <li><span class="label">mobile:</span>+44 (0) 7700 900418</li>
      <li><span class="label">phone:</span>+44 (0) 1632 960274</li>
      <li><span class="label">e-mail:</span>name@t4linkways.co.uk</li>
    </ul>
    <div class="gear-art" role="img" aria-label="Grey interlocking gears illustration"></div>
  </section>

  <section class="card card--back pos-b" aria-label="Back of card, version one">
    <div class="wordmark"><span class="wordmark__square"></span><span>linkways</span></div>
    <p class="web-address">www.t4linkways.co.uk</p>
  </section>

  <section class="card card--front pos-c" aria-label="Front of card, version two">
    <div class="header-band">
      <div class="wordmark"><span class="wordmark__square"></span><span>linkways</span></div>
    </div>
    <h1 class="person-name">Daniel Hartley</h1>
    <p class="job-title">network consultant</p>
    <ul class="contact-list">
      <li><span class="label">mobile:</span>+44 (0) 7700 900418</li>
      <li><span class="label">phone:</span>+44 (0) 1632 960274</li>
      <li><span class="label">e-mail:</span>name@t4linkways.co.uk</li>
    </ul>
  </section>

  <section class="card card--back pos-d" aria-label="Back of card, version two">
    <div class="wordmark"><span class="wordmark__square"></span><span>linkways</span></div>
    <p class="tagline">IT networking and network security solutions</p>
  </section>

</main>
</body>
</html>
```